2016 Catalog Creative Templates for text pages. Needing updated color pallet and fresh ideas

Adding a few additional comments:
Not too busy on the cover - in other words try to keep consistent and not lots of different ideas going on.

Page numbers - need to not make these large, but keep a readable size.

No need to list product categories on each page, listing once on our tab for the large catalog and this will be listed on the cover for the different books.

We are looking for creative ideas for layout design templates for our upcoming catalogs. In general all of our catalog will follow the same layout template, just slight changes to colors used in each section or catalog. Ideally, I would need one great design for a spread in our books, and a great color pallet for all the other sections and catalogs.
We are a manufacturer of mirrors, art, wall decor, lamps, lighting fixtures, rugs and accent furniture. I will be attaching current catalog layouts for reference. We prefer to keep design fairly simple on the text pages, using neutral colors throughout, this allows for our products to be the main focus in the catalogs. The catalogs that are separate books, we like keeping the color scheme the same as the wall decor book. Meaning using similar, neutral colors and design aspects. We also like to keep items to scale on pages as close as possible, on all of our books.

We have several catalogs, below is a brief description.

Wall Decor book - this is consists of 6 sections. Mirrors, Alternative Wall Decor, Clocks, Art, Accessories and Index, Each are separated by tab pages.
Accent Furniture - throughout this book, we try to use a lot of beauty and detail shots to enhance the beauty of this book, and to show we have other coordinating product. We do this in other books, just not as much. With so many product skews, it makes it very difficult to allow for this in other books.
Lamp Catalog - With this book it's also difficult to use lots of beauty shots as we have so many skews, like to keep scale fairly close on items.
Rug Catalog - sample pages attached
Lighting Catalog - sample attached

Catalog Covers - I have attached a few versions from the past few years. The 2015, the globe on the front isn't printed gray, this was used for placement and size as it was embossed. On the ones with color images, we spot gloss, varnished just the images and printed background with as a matte finish.

Thanks
Denise Halloway
Updates

Adding a few additional comments: Not too busy on the cover - in other words try to keep consistent and not lots of different ideas going on. Page numbers - need to not make these large, but keep a readable size. No need to list product categories on each page, listing once on our tab for the large catalog and this will be listed on the cover for the different books.

Guys, I really am not concerned with the deadline, I would rather get a great catalog design.

Target Market(s)

Wholesale industry customers, designers, etc.

Requirements
Must have
• Must have great, neutral colors, template ideas need to allow for product to be set up to scale.
Should not have
• Bright, neon colors. We generally stick to a neutral color pallet. Open to suggestions of colors, just not too far out of the box.

```html
<!DOCTYPE html>
<html lang="en">
<head>
<meta charset="utf-8">
<title>Catalog Spread – Brand Color Scheme</title>
<link href="https://fonts.googleapis.com/css2?family=Nunito+Sans:wght@400;700;800;900&display=swap" rel="stylesheet">
<style>
  :root {
    --ink: #000000;
    --paper: #ffffff;
    --band: #ececec;
    --heading: #555555;
    --sage: #88a59a;
    --ivory: #f0f0ee;
    --forest: #4a6f61;
    --s1-a: #dab5a7; --s1-b: #eef2e4; --s1-c: #6b8f86;
    --s2-a: #722b2d; --s2-b: #f2e3d8; --s2-c: #f3d7a6;
    --s3-a: #162340; --s3-b: #e1e7f4; --s3-c: #8b7a5a;
    --s4-a: #724a62; --s4-b: #eff0e4; --s4-c: #e6f1cc;
  }
  * { margin: 0; padding: 0; box-sizing: border-box; }
  html, body { width: 1200px; height: 1000px; overflow: hidden; background: var(--paper); }
  body { font-family: "Nunito Sans", Arial, sans-serif; }
  .spread { position: relative; width: 1200px; height: 1000px; }
  .abs { position: absolute; }

  .rule-top { left: 0; top: 125px; width: 1200px; height: 4px; background: var(--ink); }
  .rule-bottom { left: 0; top: 822px; width: 1200px; height: 2px; background: var(--ink); }
  .gutter { left: 599px; top: 125px; width: 2px; height: 710px; background: var(--ink); }
  .band { left: 0; top: 379px; width: 1200px; height: 242px; background: var(--band); }

  .title-bar { left: 100px; top: 170px; width: 1100px; height: 26px; background: var(--ink);
    color: var(--paper); font-weight: 800; font-size: 22px; line-height: 28px; padding-left: 10px; letter-spacing: 0.2px; }
  .section-icon { left: 18px; top: 143px; width: 82px; height: 82px; border-radius: 50%; background: var(--ink);
    color: var(--paper); font-size: 10.5px; line-height: 13px; text-align: center;
    display: flex; align-items: center; justify-content: center; }

  .swatch-lg { width: 218px; height: 243px; }
  .swatch-sage { left: 77px; top: 251px; background: var(--sage); }
  .swatch-ivory { left: 306px; top: 251px; background: var(--ivory); border: 2px solid var(--ink); }
  .swatch-forest { left: 77px; top: 506px; height: 242px; background: var(--forest); }

  .brand-heading { left: 305px; top: 538px; width: 220px; text-align: center; color: var(--heading);
    font-weight: 800; font-size: 52px; line-height: 64px; }

  .scheme-row { left: 677px; width: 480px; height: 65px; display: flex; align-items: center; }
  .chip { width: 65px; height: 65px; margin-right: 11px; flex: none; }
  .scheme-label { margin-left: 37px; color: var(--heading); font-weight: 800; font-size: 28px; }
  .row-1 { top: 278px; } .row-2 { top: 403px; } .row-3 { top: 528px; } .row-4 { top: 657px; }

  .footer { left: 0; top: 835px; width: 1200px; height: 41px; background: var(--ink); color: var(--paper);
    font-size: 12px; }
  .folio, .running-head { position: absolute; top: 0; line-height: 36px; }
  .folio { font-size: 14px; }
  .folio-left { left: 18px; } .running-left { left: 55px; }
  .running-right { right: 56px; } .folio-right { right: 17px; }
</style>
</head>
<body>
<div class="spread">
  <div class="abs band"></div>
  <div class="abs rule-top"></div>
  <div class="abs gutter"></div>
  <div class="abs rule-bottom"></div>

  <div class="abs title-bar">PRODUCT NAME(S)</div>
  <div class="abs section-icon">SECTION/<br>PRODUCT<br>ICON</div>

  <div class="abs swatch-lg swatch-sage"></div>
  <div class="abs swatch-lg swatch-ivory"></div>
  <div class="abs swatch-lg swatch-forest"></div>
  <div class="abs brand-heading">Brand<br>Color<br>Scheme</div>

  <div class="abs scheme-row row-1">
    <span class="chip" style="background:var(--s1-a)"></span><span class="chip" style="background:var(--s1-b)"></span><span class="chip" style="background:var(--s1-c)"></span>
    <span class="scheme-label">Scheme 1</span>
  </div>
  <div class="abs scheme-row row-2">
    <span class="chip" style="background:var(--s2-a)"></span><span class="chip" style="background:var(--s2-b)"></span><span class="chip" style="background:var(--s2-c)"></span>
    <span class="scheme-label">Scheme 2</span>
  </div>
  <div class="abs scheme-row row-3">
    <span class="chip" style="background:var(--s3-a)"></span><span class="chip" style="background:var(--s3-b)"></span><span class="chip" style="background:var(--s3-c)"></span>
    <span class="scheme-label">Scheme 3</span>
  </div>
  <div class="abs scheme-row row-4">
    <span class="chip" style="background:var(--s4-a)"></span><span class="chip" style="background:var(--s4-b)"></span><span class="chip" style="background:var(--s4-c)"></span>
    <span class="scheme-label">Scheme 4</span>
  </div>

  <div class="abs footer">
    <span class="folio folio-left">a</span>
    <span class="running-head running-left">Section Name</span>
    <span class="running-head running-right">Catalog Name</span>
    <span class="folio folio-right">b</span>
  </div>
</div>
</body>
</html>
```